Tarvell homes and renovations business card design.

Would like some new card designs utilizing my new logo that look professional. I am open to different colors on the logo or utilize the same ones we have. I like the original concept but would like to see some fresh ideas and build on what we have already done.

Target Market(s)

Custom home building industry, Real estate sales, Renovation projects.

Industry/Entity Type

Home Builder

Contact Information for Business Card

Tarvell Homes and Renovations
2871 162nd Street
Frank, Alberta
T0L3P0
Home : 403- 555-0187 Cell: 403- 555-0243

My info is : Gus Tarvell, President and CEO
email: tarvellhomes@quillmail.example
Website: tarvellhomes.example

Requirements
Must have
• Must Use my new logo design. I am open to different colors on the logo or utilize the same ones in the existing design. I can upload the original logo design if needed.

```html
<!DOCTYPE html>
<html lang="en">
<head>
<meta charset="utf-8">
<title>Tarvell Homes and Renovations – Business Card</title>
<link rel="stylesheet" href="https://fonts.googleapis.com/css2?family=Arimo:wght@400;700&family=Montserrat:wght@500&display=swap">
<style>
  :root {
    --stage: #2b2b2c;
    --gold: #b8892f;
    --gold-light: #d4a53e;
    --gold-deep: #9c7224;
    --paper: #ffffff;
    --paper-shade: #eeeeee;
    --ink: #1e1e1e;
  }
  * { box-sizing: border-box; margin: 0; padding: 0; }
  html, body { width: 1200px; height: 997px; overflow: hidden; }
  body {
    background: var(--stage);
    font-family: "Arimo", Arial, sans-serif;
    position: relative;
  }
  .card {
    position: absolute;
    left: 250px;
    width: 700px;
    height: 400px;
    border-radius: 22px;
    overflow: hidden;
  }
  .card--front {
    top: 60px;
    background: linear-gradient(160deg, var(--gold-light), var(--gold) 55%, var(--gold-deep));
    display: flex;
    align-items: center;
    justify-content: center;
    padding: 0 40px;
  }
  .card--back {
    top: 537px;
    background: linear-gradient(180deg, var(--paper), var(--paper-shade));
  }
  .wordmark {
    display: flex;
    align-items: center;
    gap: 14px;
    font-family: "Montserrat", Arial, sans-serif;
    font-weight: 500;
    text-transform: uppercase;
    white-space: nowrap;
  }
  .wordmark__square { width: 16px; height: 16px; flex: none; }
  .wordmark--light { color: var(--paper); font-size: 28px; letter-spacing: 1.5px; }
  .wordmark--light .wordmark__square { background: var(--paper); }
  .wordmark--gold {
    color: var(--gold);
    font-size: 22px;
    letter-spacing: 2px;
    position: absolute;
    top: 70px;
    left: 0; right: 0;
    justify-content: center;
  }
  .wordmark--gold .wordmark__square { background: var(--gold); width: 12px; height: 12px; }
  .card__art { position: absolute; inset: 0; }
  .person { position: absolute; left: 40px; top: 180px; }
  .person__name { color: var(--gold); font-weight: 700; font-size: 19px; }
  .person__title { color: var(--ink); font-size: 17px; margin-top: 4px; }
  .company {
    position: absolute;
    right: 30px;
    top: 228px;
    text-align: right;
    font-weight: 700;
  }
  .company__name { color: var(--gold); font-size: 16px; }
  .company__address { color: var(--ink); font-size: 14px; margin-top: 4px; line-height: 1.35; }
  .contacts { position: absolute; left: 40px; top: 276px; list-style: none; }
  .contacts li {
    display: flex; align-items: center; gap: 10px;
    font-size: 17px; color: var(--ink); height: 27px;
  }
  .contacts svg { width: 18px; height: 18px; flex: none; }
  .website {
    position: absolute;
    right: 30px;
    top: 346px;
    color: var(--paper);
    font-weight: 700;
    font-size: 16px;
    letter-spacing: 1px;
    white-space: nowrap;
  }
</style>
</head>
<body>
  <section class="card card--front">
    <div class="wordmark wordmark--light">
      <span class="wordmark__square"></span>
      <span>Tarvell Homes and Renovations</span>
    </div>
  </section>

  <section class="card card--back">
    <svg class="card__art" viewBox="0 0 700 400" aria-hidden="true">
      <line x1="232" y1="198" x2="670" y2="198" stroke="var(--gold)" stroke-width="2.5"/>
      <path d="M370 400 C400 400 400 312 440 312 L700 312 L700 400 Z" fill="var(--gold)"/>
      <path d="M0 372 L372 362 L368 370 L0 380 Z" fill="var(--gold-light)"/>
      <rect x="0" y="386" width="390" height="14" fill="var(--gold)"/>
    </svg>

    <div class="wordmark wordmark--gold">
      <span class="wordmark__square"></span>
      <span>Tarvell Homes and Renovations</span>
    </div>

    <div class="person">
      <p class="person__name">GUS TARVELL</p>
      <p class="person__title">PRESIDENT AND CEO</p>
    </div>

    <div class="company">
      <p class="company__name">TARVELL HOMES AND RENOVATIONS</p>
      <p class="company__address">2871 162nd Street Frank, Alberta<br>T0L3P0</p>
    </div>

    <ul class="contacts">
      <li>
        <svg viewBox="0 0 18 18" aria-label="Home phone"><circle cx="9" cy="9" r="9" fill="var(--gold)"/><path d="M5 7 Q9 4 13 7 L12 9 L10 8 L8 8 L6 9 Z M6 10 H12 V13 H6 Z" fill="#fff"/></svg>
        <span>403- 555-0187</span>
      </li>
      <li>
        <svg viewBox="0 0 18 18" aria-label="Cell phone"><circle cx="9" cy="9" r="9" fill="var(--gold)"/><rect x="6.5" y="4" width="5" height="10" rx="1" fill="#fff"/></svg>
        <span>403- 555-0243</span>
      </li>
      <li>
        <svg viewBox="0 0 18 18" aria-label="Email"><circle cx="9" cy="9" r="9" fill="var(--gold)"/><rect x="4.5" y="6" width="9" height="6" fill="#fff"/><path d="M4.5 6 L9 9.5 L13.5 6" fill="none" stroke="var(--gold)" stroke-width="1"/></svg>
        <span>tarvellhomes@quillmail.example</span>
      </li>
    </ul>

    <p class="website">www.tarvellhomes.example</p>
  </section>
</body>
</html>
```